Valdora necesita diseños de papeleria como tarjeta de presentacion, hoja membretada, sobres...

La papelería corporativa es para una tienda de moda multimarcas ubicada en Ecuador.
Los diseños tienen que ser de acuerdo a los diseños que adjunto.

```html
<!DOCTYPE html>
<html lang="es">
<head>
<meta charset="utf-8">
<title>Valdora – Papelería corporativa</title>
<link rel="stylesheet" href="https://fonts.googleapis.com/css2?family=Montserrat:wght@400;500;600;700&family=Work+Sans:wght@400&display=swap">
<style>
:root{
  --bg:#c6d3d0;
  --paper:#ffffff;
  --ink:#2d3236;
  --body:#6b6f73;
  --red:#e8141b;
  --rule:#3a3f43;
}
*{margin:0;padding:0;box-sizing:border-box}
html,body{width:1200px;height:836px;overflow:hidden;background:var(--bg)}
body{position:relative;font-family:"Montserrat",sans-serif;color:var(--ink)}
.sheet{position:absolute;background:var(--paper);box-shadow:2px 2px 4px rgba(0,0,0,.18);overflow:hidden}
.brand{position:absolute;text-align:center;line-height:1}
.brand-name{display:block;font-family:"Montserrat",sans-serif;font-weight:600;letter-spacing:.24em;color:var(--ink)}
.brand-tag{display:block;font-weight:500;letter-spacing:.28em;color:var(--ink)}
.brand.light .brand-name,.brand.light .brand-tag{color:#fff}
.contacts{position:absolute;list-style:none}
.contacts li{display:flex;align-items:center;white-space:nowrap}
.contacts svg{fill:var(--red);flex:none}
.contacts .hl{color:var(--red)}
.address{position:absolute;text-align:right;white-space:nowrap}
.rule{position:absolute;height:1px;background:var(--rule)}
.footer{position:absolute;left:0;bottom:0;display:block}

/* Letterhead */
.letterhead{left:66px;top:58px;width:508px;height:720px}
.letterhead .brand{left:35px;top:31px}
.letterhead .brand-name{font-size:21px}
.letterhead .brand-tag{font-size:9px;margin-top:5px}
.letter{position:absolute;left:35px;top:169px;width:440px;font-family:"Work Sans",sans-serif;color:var(--body)}
.letter .greeting{font-family:"Montserrat",sans-serif;font-size:11.5px;line-height:14px;margin-bottom:24px}
.letter .para{font-size:9.4px;letter-spacing:-.15px;line-height:13.3px;margin-bottom:15.7px}
.letter .ln{display:block;white-space:nowrap}
.signoff{position:absolute;left:35px;top:504px;color:var(--body)}
.signoff .closing{font-size:11.5px;line-height:14px;margin-bottom:7px}
.signoff .name{font-size:11.5px;line-height:14px;letter-spacing:.02em}
.signoff .role{font-size:8.5px;line-height:10px}
.letterhead .rule{left:35px;right:35px;top:625px}
.letterhead .contacts{left:35px;top:643px;font-size:9.2px;font-weight:500}
.letterhead .contacts li{height:11.2px}
.letterhead .contacts svg{width:6px;height:6px;margin-right:3px}
.letterhead .address{right:35px;top:665px;font-size:9.2px;font-weight:500;line-height:11.2px}

/* Business card */
.card-front{left:614px;top:58px;width:247px;height:141px}
.card-front .brand{right:10px;top:10px}
.card-front .brand-name{font-size:11.5px;letter-spacing:.2em}
.card-front .brand-tag{font-size:5.5px;margin-top:2px;letter-spacing:.26em}
.card-front .marker{position:absolute;left:0;top:59px;width:3px;height:15px;background:var(--red)}
.card-front .person{position:absolute;left:10px;top:58px;line-height:1}
.card-front .person-name{font-size:10px;font-weight:700;color:var(--red);letter-spacing:.08em}
.card-front .person-role{font-size:6.3px;font-weight:500;margin-top:3px}
.card-front .rule{left:10px;right:10px;top:81px;background:var(--red);height:.7px}
.card-front .contacts{left:10px;top:91px;font-size:6.3px;font-weight:500}
.card-front .contacts li{height:8.5px}
.card-front .contacts svg{width:4px;height:4px;margin-right:3px}
.card-front .address{right:10px;top:108px;font-size:6.3px;font-weight:500;line-height:8.5px}
.card-back{left:886px;top:58px;width:248px;height:141px;background:var(--ink)}
.card-back .brand{left:0;right:0;top:55px}
.card-back .brand-name{font-size:19px;letter-spacing:.22em}
.card-back .brand-tag{font-size:8px;margin-top:5px}

/* DL compliment sheet */
.compliment{left:614px;top:229px;width:518px;height:259px}
.compliment .brand{left:18px;top:17px}
.compliment .brand-name{font-size:17px;letter-spacing:.22em}
.compliment .brand-tag{font-size:7.5px;margin-top:4px}
.compliment .rule{left:19px;right:19px;top:169px}
.compliment .contacts{left:19px;top:181px;font-size:9px;font-weight:500}
.compliment .contacts li{height:11px}
.compliment .contacts svg{width:5.5px;height:5.5px;margin-right:4px}
.compliment .address{right:20px;top:203px;font-size:9px;font-weight:500;line-height:11px}

/* Envelope */
.envelope{left:615px;top:519px;width:517px;height:259px}
.envelope .flap{position:absolute;left:0;top:0}
.envelope .brand{left:0;right:0;top:20px}
.envelope .brand-name{font-size:18px;letter-spacing:.22em}
.envelope .brand-tag{font-size:7.5px;margin-top:5px}
</style>
</head>
<body>

<svg width="0" height="0" style="position:absolute" aria-hidden="true">
  <defs>
    <symbol id="i-phone" viewBox="0 0 10 10"><path d="M2.2 0.6 3.6 2.8 2.7 3.8C3.3 5.2 4.6 6.6 6.1 7.3L7.1 6.4 9.4 7.8 8.6 9.4C4.6 9.2 0.8 5.4 0.6 1.4Z"/></symbol>
    <symbol id="i-mobile" viewBox="0 0 10 10"><path d="M2.5 0H7.5V10H2.5ZM3.5 1.2V7.6H6.5V1.2Z"/></symbol>
    <symbol id="i-mail" viewBox="0 0 10 10"><path d="M0 2H10V8H0ZM1.2 3V7H8.8V3L5 5.6Z"/></symbol>
    <symbol id="i-web" viewBox="0 0 10 10"><path d="M5 0A5 5 0 1 0 5 10A5 5 0 1 0 5 0ZM1.3 4.4H3.2C3.3 3 3.6 1.9 4 1.3A3.9 3.9 0 0 0 1.3 4.4ZM4.3 4.4H5.7C5.6 2.7 5.3 1.6 5 1.2C4.7 1.6 4.4 2.7 4.3 4.4ZM6.8 4.4H8.7A3.9 3.9 0 0 0 6 1.3C6.4 1.9 6.7 3 6.8 4.4ZM1.3 5.6A3.9 3.9 0 0 0 4 8.7C3.6 8.1 3.3 7 3.2 5.6ZM4.3 5.6C4.4 7.3 4.7 8.4 5 8.8C5.3 8.4 5.6 7.3 5.7 5.6ZM6.8 5.6C6.7 7 6.4 8.1 6 8.7A3.9 3.9 0 0 0 8.7 5.6Z"/></symbol>
  </defs>
</svg>

<!-- Letterhead -->
<section class="sheet letterhead">
  <div class="brand"><span class="brand-name">VALDORA</span><span class="brand-tag">MODA &amp; LENCERIA</span></div>
  <div class="letter">
    <p class="greeting">Dear sir/Madam,</p>
    <p class="para">
      <span class="ln">Lorem ipsum dolor sit amet, an vel recteque dissentiet, detracto albucius platonem ex vel,</span>
      <span class="ln">eros repudiandae cu. Atqui aliquando nec an, unum graece adolescens vel ad. Id odio scae</span>
      <span class="ln">has, iudico euismod atomorum ius ea, cum ea honestatis quaerendum theophrastus. Mea</span>
      <span class="ln">honestatis quaerendum theophrastus. Mea</span>
    </p>
    <p class="para">
      <span class="ln">Lorem ipsum dolor sit amet, an vel recteque dissentiet, detracto albucius platonem ex vel,</span>
      <span class="ln">eros repudiandae cu. Atqui aliquando nec an, unum graece adolescens vel ad. Id odio scae</span>
      <span class="ln">has, iudico euismod atomorum ius ea, cum ea honestatis quaerendum theophrastus. Mea</span>
      <span class="ln">doming repudiandae ex, cu cum civibus assentior posidonium. Quo etiam pertinax ex, te</span>
      <span class="ln">eros repudiandae cu. Atqui aliquando nec an, unum graece adolescens vel ad. Id odio scae</span>
      <span class="ln">honestatis quaerendum theophrastus. Mea</span>
    </p>
    <p class="para">
      <span class="ln">Lorem ipsum dolor sit amet, an vel recteque dissentiet, detracto albucius platonem ex vel,</span>
      <span class="ln">eros repudiandae cu. Atqui aliquando nec an, unum graece adolescens vel ad. Id odio scae</span>
      <span class="ln">has, iudico euismod atomorum ius ea, cum ea honestatis quaerendum theophrastus. Mea</span>
      <span class="ln">honestatis quaerendum theophrastus. Mea</span>
    </p>
    <p class="para">
      <span class="ln">eros repudiandae cu. Atqui aliquando nec an, unum graece adolescens vel ad. Id odio scae</span>
      <span class="ln">honestatis quaerendum theophrastus. Mea posidonium. Quo etiam pertinax ex, te</span>
      <span class="ln">etiam pertinax ex, te</span>
    </p>
  </div>
  <div class="signoff">
    <p class="closing">Kind Regards</p>
    <p class="name">Daniel R. Cárdenas</p>
    <p class="role">CEO / Founder</p>
  </div>
  <div class="rule"></div>
  <ul class="contacts">
    <li><svg><use href="#i-phone"/></svg>+593 7 410-2268</li>
    <li><svg><use href="#i-mobile"/></svg>+593 99 517-3380</li>
    <li><svg><use href="#i-mail"/></svg>info@valdora.com</li>
    <li><svg><use href="#i-web"/></svg>www.<span class="hl">valdora</span>.com</li>
  </ul>
  <p class="address">Av. Las Palmas y Sucre.<br>Machala, Ecuador</p>
  <svg class="footer" width="508" height="26" viewBox="0 0 508 26" aria-hidden="true">
    <path d="M0 19H268C296 19 300 4 330 4H508V26H0Z" fill="var(--ink)"/>
    <path d="M0 10H288C292 10 294 12 290 14C286 16 284 15 280 15H0Z" fill="var(--red)"/>
  </svg>
</section>

<!-- Business card front -->
<section class="sheet card-front">
  <div class="brand"><span class="brand-name">VALDORA</span><span class="brand-tag">MODA &amp; LENCERIA</span></div>
  <span class="marker"></span>
  <div class="person"><p class="person-name">ANDRÉS LOZADA</p><p class="person-role">Gerente General</p></div>
  <div class="rule"></div>
  <ul class="contacts">
    <li><svg><use href="#i-phone"/></svg>+593 7 410-2268</li>
    <li><svg><use href="#i-mobile"/></svg>+593 99 517-3380</li>
    <li><svg><use href="#i-mail"/></svg>info@valdora.com</li>
    <li><svg><use href="#i-web"/></svg>www.<span class="hl">valdora</span>.com</li>
  </ul>
  <p class="address">Av. Las Palmas y Sucre.<br>Machala, Ecuador</p>
  <svg class="footer" width="247" height="12" viewBox="0 0 247 12" aria-hidden="true">
    <path d="M0 9H138C150 9 152 1 166 1H247V12H0Z" fill="var(--ink)"/>
    <path d="M0 3H143C146 3 146 5 142 5.5H0Z" fill="var(--red)"/>
  </svg>
</section>

<!-- Business card back -->
<section class="sheet card-back">
  <div class="brand light"><span class="brand-name">VALDORA</span><span class="brand-tag">MODA &amp; LENCERIA</span></div>
</section>

<!-- Compliment slip -->
<section class="sheet compliment">
  <div class="brand"><span class="brand-name">VALDORA</span><span class="brand-tag">MODA &amp; LENCERIA</span></div>
  <div class="rule"></div>
  <ul class="contacts">
    <li><svg><use href="#i-phone"/></svg>+593 7 410-2268</li>
    <li><svg><use href="#i-mobile"/></svg>+593 99 517-3380</li>
    <li><svg><use href="#i-mail"/></svg>info@valdora.com</li>
    <li><svg><use href="#i-web"/></svg>www.<span class="hl">valdora</span>.com</li>
  </ul>
  <p class="address">Av. Las Palmas y Sucre.<br>Machala, Ecuador</p>
  <svg class="footer" width="518" height="24" viewBox="0 0 518 24" aria-hidden="true">
    <path d="M0 17H290C312 17 318 1 345 1H518V24H0Z" fill="var(--ink)"/>
    <path d="M0 6H300C304 6 305 8 300 10H0Z" fill="var(--red)"/>
  </svg>
</section>

<!-- Envelope -->
<section class="sheet envelope">
  <svg class="flap" width="517" height="67" viewBox="0 0 517 67" aria-hidden="true">
    <path d="M0 0H517L508 42C504 58 492 66 470 66H47C25 66 13 58 9 42Z" fill="var(--ink)"/>
  </svg>
  <div class="brand light"><span class="brand-name">VALDORA</span><span class="brand-tag">MODA &amp; LENCERIA</span></div>
</section>

</body>
</html>
```